Lucky Orbit Fun Casino Entertainment

Looking to update my business card and make it look more modern, stand out and eye catching.
We are are fun casino business in Australia (primarily Sydney). Blackjack and Roulette are our most popular games although we have pretty much every game available for hire that you would find in a real casino. The final design would need to be sleek and appeal to the more upmarket corporate sector.
We mainly cater for Corporate Events, Private Parties, Fundraising Events, Team Building, Poker Tournaments
I think I'd prefer the colour Black.

Target Market(s)

High-end Corporate

Industry/Entity Type

Events

Contact Information for Business Card

Dale Hutchins
Director
1300 482 617
0431 758 209
info@luckyorbit.com.au
www.luckyorbit.com.au
Facebook & Instagram @luckyorbitshows (proper social icons preferred)

Colors
000000
0255a3

Requirements
Must have
• Front side:
• Logo
• Contact details
• 'Australia's #1 Fun Casino Specialists'
• Back:
• Logo
Nice to have
• Back:
• Corporate Events
• Private Parties
• Poker Tournaments
• Fundraising
• Props & Theming
• Photo Booth
• Horse Racing Events
• The Vegas Sign attached, maybe on the back of the card in the background...?

```html
<!DOCTYPE html>
<html lang="en">
<head>
<meta charset="utf-8">
<title>Lucky Orbit – Business Card</title>
<link href="https://fonts.googleapis.com/css2?family=Open+Sans:wght@400;700;800&display=swap" rel="stylesheet">
<style>
  :root {
    --ink: #000000;
    --brand-blue: #0255a3;
    --ray-blue: #0a5fc0;
    --paper: #ffffff;
    --stage: #2e3033;
    --text-light: #ffffff;
    --logo-ink: #1c1c1c;
    --accent: #f5a21b;
  }
  * { box-sizing: border-box; margin: 0; padding: 0; }
  html, body { width: 1200px; height: 900px; overflow: hidden; }
  body {
    background: var(--stage);
    font-family: "Open Sans", Arial, sans-serif;
    display: flex;
    align-items: center;
    justify-content: center;
    gap: 80px;
  }
  .card {
    position: relative;
    width: 360px;
    height: 580px;
    border-radius: 22px;
    overflow: hidden;
    background: var(--ink);
  }
  .card-rays { position: absolute; inset: 0; width: 100%; height: 100%; }
  .logo-disc {
    position: absolute;
    left: 50%;
    width: 240px;
    height: 240px;
    margin-left: -120px;
    border-radius: 50%;
    background: var(--paper);
    box-shadow: 0 0 14px rgba(255,255,255,0.6);
    display: flex;
    align-items: center;
    justify-content: center;
    gap: 10px;
  }
  .card-front .logo-disc { top: 36px; }
  .card-back .logo-disc { top: 155px; width: 270px; height: 270px; margin-left: -135px; }
  .logo-dot {
    width: 18px; height: 18px; border-radius: 50%;
    background: var(--accent);
    flex: none;
  }
  .logo-name {
    color: var(--logo-ink);
    font-weight: 800;
    font-size: 30px;
    line-height: 1.05;
    text-transform: uppercase;
  }
  .contact-panel {
    position: absolute;
    left: 0; right: 0; bottom: 0;
    height: 290px;
    padding: 26px 24px 0 34px;
    color: var(--text-light);
  }
  .person-name { font-size: 34px; font-weight: 800; line-height: 1; }
  .person-role { font-size: 16px; margin-top: 4px; margin-bottom: 16px; }
  .contact-list { list-style: none; }
  .contact-item {
    display: flex;
    align-items: flex-start;
    gap: 14px;
    font-size: 13px;
    line-height: 1.3;
    margin-bottom: 9px;
  }
  .contact-icon { width: 18px; height: 18px; flex: none; margin-top: 0; }
  .tagline {
    position: absolute;
    left: 50%;
    bottom: 42px;
    transform: translateX(-50%);
    white-space: nowrap;
    background: var(--ink);
    color: var(--text-light);
    font-size: 15px;
    font-weight: 700;
    padding: 8px 16px;
    border-radius: 18px;
  }
</style>
</head>
<body>

  <section class="card card-front" aria-label="Business card front">
    <svg class="card-rays" viewBox="0 0 360 580" aria-hidden="true">
      <rect width="360" height="580" fill="var(--ink)"/>
      <polygon points="180,155 0,40 0,130" fill="var(--ray-blue)"/>
      <polygon points="180,155 130,0 220,0" fill="var(--ray-blue)"/>
      <polygon points="180,155 360,60 360,150" fill="var(--ray-blue)"/>
      <polygon points="0,300 360,215 360,580 0,580" fill="var(--brand-blue)"/>
    </svg>
    <div class="logo-disc">
      <span class="logo-dot"></span>
      <span class="logo-name">Lucky<br>Orbit</span>
    </div>
    <div class="contact-panel">
      <h1 class="person-name">Dale Hutchins</h1>
      <p class="person-role">Director</p>
      <ul class="contact-list">
        <li class="contact-item">
          <svg class="contact-icon" viewBox="0 0 20 20" aria-hidden="true"><rect x="1" y="4" width="18" height="12" fill="none" stroke="#fff" stroke-width="1.8"/><polyline points="1,4 10,11 19,4" fill="none" stroke="#fff" stroke-width="1.8"/></svg>
          <span>info@luckyorbit.com.au</span>
        </li>
        <li class="contact-item">
          <svg class="contact-icon" viewBox="0 0 20 20" aria-hidden="true"><path d="M5 2l3 4-2 2c1 2 3 4 5 5l2-2 4 3-2 3C9 17 3 11 2 5z" fill="#fff"/></svg>
          <span>1300 482 617<br>0431 758 209</span>
        </li>
        <li class="contact-item">
          <svg class="contact-icon" viewBox="0 0 20 20" aria-hidden="true"><circle cx="10" cy="10" r="8" fill="none" stroke="#fff" stroke-width="1.6"/><ellipse cx="10" cy="10" rx="3.5" ry="8" fill="none" stroke="#fff" stroke-width="1.4"/><line x1="2" y1="10" x2="18" y2="10" stroke="#fff" stroke-width="1.4"/></svg>
          <span>www.luckyorbit.com.au</span>
        </li>
        <li class="contact-item">
          <svg class="contact-icon" viewBox="0 0 20 20" aria-hidden="true"><path d="M3 4h14v9H9l-4 3v-3H3z" fill="none" stroke="#fff" stroke-width="1.7" stroke-linejoin="round"/></svg>
          <span>lucky orbit</span>
        </li>
        <li class="contact-item">
          <svg class="contact-icon" viewBox="0 0 20 20" aria-hidden="true"><path d="M8 12l4-4M7 9l-2 2a2.8 2.8 0 0 0 4 4l2-2M13 11l2-2a2.8 2.8 0 0 0-4-4L9 7" fill="none" stroke="#fff" stroke-width="1.7" stroke-linecap="round"/></svg>
          <span>@luckyorbitshows</span>
        </li>
      </ul>
    </div>
  </section>

  <section class="card card-back" aria-label="Business card back">
    <svg class="card-rays" viewBox="0 0 360 580" aria-hidden="true">
      <rect width="360" height="580" fill="var(--ink)"/>
      <polygon points="180,290 0,20 0,110" fill="var(--ray-blue)"/>
      <polygon points="180,290 0,200 0,270" fill="var(--ray-blue)"/>
      <polygon points="180,290 0,420 0,500" fill="var(--ray-blue)"/>
      <polygon points="180,290 120,580 210,580" fill="var(--ray-blue)"/>
      <polygon points="180,290 360,470 360,560" fill="var(--ray-blue)"/>
      <polygon points="180,290 360,240 360,320" fill="var(--ray-blue)"/>
      <polygon points="180,290 300,0 360,0 360,60" fill="var(--ray-blue)"/>
    </svg>
    <div class="logo-disc">
      <span class="logo-dot"></span>
      <span class="logo-name">Lucky<br>Orbit</span>
    </div>
    <p class="tagline">Australia's #1 Fun Casino Specialists</p>
  </section>

</body>
</html>
```